Cedar nest sal
Affordable luxury
Professional
Paul dorsey
Doesn't matter, just write anything, will finalize later
Pauldorsey@quillmarsh.net
All I need is a template that suits the logo, I expect a draft template from your side.
It should include, the name, title, company logo, subtitle, website address, physical address, phone number and email. Thank you
Please suggest
Design number 1 will be used
red as second option

```html
<!DOCTYPE html>
<html lang="en">
<head>
<meta charset="utf-8">
<title>Cedar Nest Sal – Stationery</title>
<link rel="stylesheet" href="https://fonts.googleapis.com/css2?family=Cinzel:wght@600&family=Open+Sans:wght@400;600&display=swap">
<style>
  :root {
    --canvas: #b3b3b5;
    --paper: #ffffff;
    --brown: #6a3a14;
    --brown-dark: #55300f;
    --olive: #6f8b2b;
    --swoosh: #a2a2a5;
    --ink: #3c3c3c;
    --edge: #c9c9c9;
  }
  html, body { margin: 0; padding: 0; overflow: hidden; }
  body {
    width: 1200px; height: 626px;
    background: var(--canvas);
    position: relative;
    font-family: "Open Sans", Arial, sans-serif;
    color: var(--ink);
  }
  .sheet {
    position: absolute;
    background: var(--paper);
    box-shadow: 0 0 0 1px var(--edge);
    overflow: hidden;
  }
  .sheet svg.trim { position: absolute; inset: 0; width: 100%; height: 100%; }
  .brand {
    position: absolute;
    display: flex; align-items: center; gap: 5px;
    font-family: "Cinzel", Georgia, serif;
    font-weight: 600;
    color: var(--brown);
    white-space: nowrap;
  }
  .brand-square { background: var(--brown); display: inline-block; }
  .contact {
    position: absolute;
    margin: 0;
    font-size: 5.5px;
    line-height: 1.5;
    color: var(--ink);
  }

  /* Business cards */
  .card-front { left: 34px; top: 194px; width: 184px; height: 104px; }
  .card-front .brand { left: 42px; top: 40px; font-size: 14px; }
  .card-front .brand-square { width: 12px; height: 12px; }

  .card-back { left: 34px; top: 310px; width: 184px; height: 104px; }
  .card-back .brand { left: 10px; top: 12px; font-size: 9px; }
  .card-back .brand-square { width: 8px; height: 8px; }
  .card-back .person { position: absolute; left: 96px; top: 38px; font-size: 5.5px; line-height: 1.5; margin: 0; }
  .card-back .person strong { font-weight: 600; display: block; }
  .card-back .contact { left: 10px; top: 48px; }

  /* Letterhead */
  .letterhead { left: 233px; top: 29px; width: 432px; height: 578px; }
  .letterhead .brand { left: 22px; top: 28px; font-size: 15px; }
  .letterhead .brand-square { width: 13px; height: 13px; }
  .letterhead .site { position: absolute; left: 44px; top: 92px; font-size: 5px; margin: 0; }
  .letterhead .contact { left: 22px; top: 520px; }

  /* Envelope back */
  .envelope-back { left: 679px; top: 79px; width: 487px; height: 233px; }

  /* Envelope front */
  .envelope-front { left: 679px; top: 336px; width: 487px; height: 271px; }
  .envelope-front .brand { left: 26px; top: 40px; font-size: 14px; }
  .envelope-front .brand-square { width: 12px; height: 12px; }
  .envelope-front .contact { left: 18px; top: 108px; }
</style>
</head>
<body>

<svg width="0" height="0" style="position:absolute" aria-hidden="true">
  <defs>
    <linearGradient id="band-vertical" x1="0" y1="0" x2="0" y2="1">
      <stop offset="0" stop-color="#6a3a14"/>
      <stop offset="0.45" stop-color="#6f8b2b"/>
      <stop offset="1" stop-color="#5a3210"/>
    </linearGradient>
    <radialGradient id="flap-glow" cx="0.5" cy="0.45" r="0.55">
      <stop offset="0" stop-color="#6f8b2b"/>
      <stop offset="1" stop-color="#6a3a14"/>
    </radialGradient>
  </defs>
</svg>

<!-- Business card front -->
<section class="sheet card-front">
  <div class="brand"><span class="brand-square"></span>Cedar Nest Sal</div>
</section>

<!-- Business card back -->
<section class="sheet card-back">
  <svg class="trim" viewBox="0 0 184 104" preserveAspectRatio="none" aria-hidden="true">
    <path d="M150 0 H184 V104 H172 C150 80 146 30 150 0 Z" fill="url(#band-vertical)"/>
    <path d="M130 104 C160 96 176 80 184 60 V104 Z" fill="var(--swoosh)"/>
  </svg>
  <div class="brand"><span class="brand-square"></span>Cedar Nest Sal</div>
  <p class="person"><strong>Paul dorsey</strong>Sales Director</p>
  <p class="contact">
    Tel 04 528 317<br>Fax 04 528 318<br>Mob 03 672 194<br>
    12 Pine Road, Baabda<br>www.cedarnestsal.com<br>Pauldorsey@quillmarsh.net
  </p>
</section>

<!-- Letterhead -->
<section class="sheet letterhead">
  <svg class="trim" viewBox="0 0 432 578" preserveAspectRatio="none" aria-hidden="true">
    <path d="M398 0 H432 V578 H420 C392 420 386 200 398 0 Z" fill="url(#band-vertical)"/>
    <path d="M250 578 C340 560 410 520 432 450 V578 Z" fill="var(--swoosh)"/>
  </svg>
  <div class="brand"><span class="brand-square"></span>Cedar Nest Sal</div>
  <p class="site">www.cedarnestsal.com</p>
  <p class="contact">
    Tel 04 528 317<br>Fax 04 528 318<br>Mob 03 672 194<br>
    12 Pine Road, Baabda<br>www.cedarnestsal.com<br>Pauldorsey@quillmarsh.net
  </p>
</section>

<!-- Envelope back -->
<section class="sheet envelope-back">
  <svg class="trim" viewBox="0 0 487 233" preserveAspectRatio="none" aria-hidden="true">
    <polygon points="0,0 487,0 487,60 243.5,74 0,60" fill="url(#flap-glow)"/>
    <polyline points="0,60 243.5,74 487,60" fill="none" stroke="#e2e2e2" stroke-width="1"/>
  </svg>
</section>

<!-- Envelope front -->
<section class="sheet envelope-front">
  <svg class="trim" viewBox="0 0 487 271" preserveAspectRatio="none" aria-hidden="true">
    <path d="M440 0 H487 V271 H474 C440 190 430 80 440 0 Z" fill="url(#band-vertical)"/>
    <path d="M300 271 C400 258 470 220 487 170 V271 Z" fill="var(--swoosh)"/>
  </svg>
  <div class="brand"><span class="brand-square"></span>Cedar Nest Sal</div>
  <p class="contact">
    Tel 04 528 317<br>Fax 04 528 318<br>Mob 03 672 194<br>
    12 Pine Road, Baabda<br>www.cedarnestsal.com<br>Pauldorsey@quillmarsh.net
  </p>
</section>

</body>
</html>
```